Boutique custom software development company needs new business card

Our nearly 20 year old custom software development company would like to better include the fact that we are now providing Bitcoin services. These new services are B2B include education (how to acquire and securely hold Bitcoin) and integrating Bitcoin payments into existing ecommerce sites or other existing systems. Please keep the card clean and simple. Attached is our current design and some other files. velquor.example

Target Market(s)

businesses owners interested in long term relationship

Industry/Entity Type

Custom software development and Bitcoin

Contact Information for Business Card

Dale Furness, dale@velquor.example, velquor.example, (555) 274-VELQ

Font styles to use
Other font styles liked:
• monospace

Requirements
Must have
• double-sided
Nice to have
• clean and simple
Should not have
• physical address

```html
<!DOCTYPE html>
<html lang="en">
<head>
<meta charset="utf-8">
<title>Velquor Business Card</title>
<link href="https://fonts.googleapis.com/css2?family=Lato:wght@400&family=Montserrat:wght@400;600;700&display=swap" rel="stylesheet">
<style>
  :root {
    --stage: #6e5640;
    --card-white: #ffffff;
    --brand-blue: #3a70b8;
    --brand-blue-light: #8fb3e3;
    --brand-blue-dark: #24569b;
    --brand-orange: #ef7d22;
    --text-white: #ffffff;
  }
  * { box-sizing: border-box; margin: 0; padding: 0; }
  html, body { width: 900px; height: 1200px; overflow: hidden; }
  body {
    background: var(--stage);
    font-family: "Montserrat", sans-serif;
    position: relative;
  }
  .card {
    position: absolute;
    left: 80px;
    width: 742px;
    height: 442px;
    border-radius: 30px;
    overflow: hidden;
  }
  .card-front { top: 130px; background: var(--card-white); }
  .card-back { top: 637px; background: var(--brand-blue); }

  .brand { position: absolute; display: flex; align-items: center; }
  .brand-square { background: var(--brand-blue); flex: none; }
  .brand-text { display: flex; flex-direction: column; }
  .brand-name {
    font-family: "Montserrat", sans-serif;
    font-weight: 700;
    letter-spacing: 1px;
    line-height: 1;
    white-space: nowrap;
  }
  .brand-tagline {
    font-family: "Lato", sans-serif;
    font-weight: 400;
    white-space: nowrap;
  }

  .card-front .brand { left: 110px; top: 78px; }
  .card-front .brand-square { width: 125px; height: 122px; margin-right: 33px; }
  .card-front .brand-name { font-size: 60px; color: var(--brand-blue); }
  .card-front .brand-tagline { font-size: 20px; color: var(--brand-blue); margin-top: 10px; letter-spacing: -0.4px; padding-left: 14px; }

  .accent-rule {
    position: absolute; left: 0; top: 253px;
    width: 100%; height: 10px; background: var(--brand-orange);
  }
  .contact-band {
    position: absolute; left: 0; top: 274px;
    width: 100%; height: 129px; background: var(--brand-blue);
  }
  .person {
    position: absolute; right: 414px; top: 32px; text-align: right;
  }
  .person-name { font-size: 25px; font-weight: 700; color: var(--brand-orange); line-height: 1.1; white-space: nowrap; }
  .person-role { font-size: 15px; color: var(--text-white); margin-top: 4px; }
  .divider {
    position: absolute; left: 363px; top: 24px;
    width: 2px; height: 60px; background: var(--brand-orange);
  }
  .contact-list { position: absolute; left: 390px; top: 22px; list-style: none; }
  .contact-list li {
    display: flex; align-items: center; height: 22.5px;
    font-size: 15.5px; color: var(--text-white); white-space: nowrap;
  }
  .contact-list svg { width: 12px; height: 12px; margin-right: 13px; flex: none; }

  .back-pattern {
    position: absolute; inset: 0;
    background: linear-gradient(90deg, var(--brand-blue-light) 0%, var(--brand-blue) 55%, var(--brand-blue-dark) 100%);
    opacity: 0.55;
  }
  .card-back .brand { left: 287px; top: 280px; }
  .card-back .brand-square { width: 68px; height: 68px; background: var(--card-white); margin-right: 17px; }
  .card-back .brand-name { font-size: 41px; color: var(--text-white); }
  .card-back .brand-tagline { font-size: 16px; color: var(--text-white); margin-top: 6px; letter-spacing: -0.3px; padding-left: 10px; }
</style>
</head>
<body>

<section class="card card-front">
  <div class="brand">
    <div class="brand-square"></div>
    <div class="brand-text">
      <span class="brand-name">VELQUOR</span>
      <span class="brand-tagline">custom software &amp; bitcoin services</span>
    </div>
  </div>

  <div class="accent-rule"></div>

  <div class="contact-band">
    <div class="person">
      <p class="person-name">Dale Furness</p>
      <p class="person-role">Owner</p>
    </div>
    <div class="divider"></div>
    <ul class="contact-list">
      <li>
        <svg viewBox="0 0 12 12" aria-hidden="true"><path fill="#ef7d22" d="M1 4c0-2 2-3 5-3s5 1 5 3v1H8V4H4v1H1zM3 6h6l1 5H2z"/></svg>
        555.274.0153
      </li>
      <li>
        <svg viewBox="0 0 12 12" aria-hidden="true"><rect x="1" y="2.5" width="10" height="7" fill="#ef7d22"/><path d="M1 3l5 4 5-4" stroke="#3a70b8" stroke-width="1" fill="none"/></svg>
        dale@velquor.example
      </li>
      <li>
        <svg viewBox="0 0 12 12" aria-hidden="true"><circle cx="6" cy="6" r="5" fill="#ef7d22"/><path d="M1 6h10M6 1c2 2 2 8 0 10M6 1c-2 2-2 8 0 10" stroke="#3a70b8" stroke-width="0.8" fill="none"/></svg>
        www.velquor.example
      </li>
    </ul>
  </div>
</section>

<section class="card card-back">
  <div class="back-pattern" role="img" aria-label="Repeating grid of brand tiles fading from light to dark blue"></div>
  <div class="brand">
    <div class="brand-square"></div>
    <div class="brand-text">
      <span class="brand-name">VELQUOR</span>
      <span class="brand-tagline">custom software &amp; bitcoin services</span>
    </div>
  </div>
</section>

</body>
</html>
```